Hey Nestbox Grows up and Wordpress website

We need a Wordpress theme design for Hey Nestbox. Hey Nestbox is a training site for people who don't know how to use Plumtree's Nestbox. We have already had a brand created and now would like that applied to a website.
A website that is easy and simple to use, that enables video viewing for public and paid subscriptions is ideal.

Reason: I am waiting on a design from someone who has yet to submit.

Target Market(s)

Mums with Tellvos, generally a female audience

Industry/Entity Type

Training

Coding

Coded - Design and coding required

Number of Pages Required

3 page

Font styles to use
Sans Serif

Colors
33a6d7
f04a50

Requirements
Must have
• Must have a section for a Jargon Buster (like an FAQ)
• Blog page
• Video feeds from Viddora or other hosting service
Nice to have
• Feeds from Social Media
• Login for Subscription to videos and other services
Should not have
• Complicated language

```html
<!DOCTYPE html>
<html lang="en">
<head>
<meta charset="utf-8">
<title>Hey Nestbox – Blog</title>
<link rel="stylesheet" href="https://fonts.googleapis.com/css2?family=Montserrat:wght@500;600;700&family=Mulish:wght@400;600&display=swap">
<style>
  :root {
    --brand-blue: #33a6d7;
    --brand-red: #f04a50;
    --panel-grey: #f0f0f0;
    --text-dark: #2b2b2b;
    --footer-bg: #3b3b3b;
    --footer-text: #d8d8d8;
    --icon-grey: #bdbdbd;
    --rule: #3a3a3a;
    --media-top: #6a6461;
    --media-bottom: #3e3029;
  }
  * { box-sizing: border-box; margin: 0; padding: 0; }
  html, body { width: 1200px; height: 1200px; overflow: hidden; background: #fff; }
  body { position: relative; font-family: "Mulish", "Helvetica Neue", sans-serif; color: var(--text-dark); }

  .site-header {
    position: absolute; left: 190px; top: 0; width: 820px; height: 62px;
    background: var(--panel-grey); border-bottom: 1.5px solid var(--rule);
  }
  .brand {
    position: absolute; left: 61px; top: 17px; display: flex; align-items: center; gap: 8px;
    font-family: "Montserrat", sans-serif; font-weight: 600; font-size: 20px; color: var(--brand-blue);
  }
  .brand-dot { width: 26px; height: 26px; border-radius: 50%; background: var(--brand-blue); }
  .main-nav { position: absolute; left: 293px; top: 23px; display: flex; gap: 17px; }
  .main-nav a, .login-link {
    font-family: "Montserrat", sans-serif; font-weight: 600; font-size: 10.5px;
    letter-spacing: 0.6px; text-decoration: none; color: var(--text-dark);
  }
  .login-link { position: absolute; left: 692px; top: 23px; color: var(--brand-red); }
  .search-icon { position: absolute; left: 749px; top: 24px; }

  .post-column {
    position: absolute; left: 250px; top: 63px; width: 486px; height: 1031px;
    background: var(--panel-grey);
  }
  .post { position: absolute; left: 6px; width: 474px; }
  .post-media {
    width: 474px; height: 182px;
    background: linear-gradient(180deg, var(--media-top) 0%, var(--media-bottom) 100%);
  }
  .post-title {
    margin: 15px 0 0 2px; font-family: "Montserrat", sans-serif; font-weight: 700;
    font-size: 14.5px; letter-spacing: 0.9px; color: var(--brand-red);
  }
  .post-meta { margin: 15px 0 0 3px; font-size: 10.5px; letter-spacing: 0.8px; }
  .post-meta a { color: var(--brand-blue); text-decoration: none; }
  .post-excerpt { margin: 4px 0 0 3px; width: 470px; font-size: 10px; line-height: 15.6px; letter-spacing: 0.45px; }
  .post-excerpt span { display: block; white-space: nowrap; }

  .sidebar {
    position: absolute; left: 736px; top: 63px; width: 215px; height: 215px;
    background: var(--brand-red); color: #fff;
    display: flex; align-items: center; justify-content: center;
    font-family: "Montserrat", sans-serif; font-weight: 500; font-size: 15px; letter-spacing: 1.2px;
  }

  .site-footer {
    position: absolute; left: 190px; top: 1146px; width: 820px; height: 54px;
    background: var(--footer-bg);
  }
  .copyright {
    position: absolute; left: 61px; top: 21px; font-size: 10.5px; letter-spacing: 0.8px; color: var(--footer-text);
  }
  .social-links { position: absolute; left: 624px; top: 13px; display: flex; gap: 7px; }
  .social-links span { width: 29px; height: 29px; background: var(--icon-grey); display: block; }
</style>
</head>
<body>
  <header class="site-header">
    <div class="brand"><span class="brand-dot"></span>Hey Nestbox</div>
    <nav class="main-nav">
      <a href="#">Home</a><a href="#">Jargon baster</a><a href="#">Videos</a><a href="#">Pricing</a>
    </nav>
    <a class="login-link" href="#">Login</a>
    <svg class="search-icon" width="11" height="11" viewBox="0 0 11 11" aria-label="Search">
      <circle cx="4.5" cy="4.5" r="3.4" fill="none" stroke="#f04a50" stroke-width="1.5"/>
      <line x1="7" y1="7" x2="10" y2="10" stroke="#f04a50" stroke-width="1.6" stroke-linecap="round"/>
    </svg>
  </header>

  <main class="post-column">
    <article class="post" style="top:5px">
      <div class="post-media" role="img" aria-label="Photo of a phone on a stand beside an open laptop on a desk"></div>
      <h2 class="post-title">Lorem ipsum Lorem ipsum Lorem.</h2>
      <p class="post-meta">by <a href="#">John</a> | Jan 27, 2017 <a href="#">California</a></p>
      <p class="post-excerpt"><span>Lorem Ipsum is simply dummy text of the printing and typesetting industry. Lorem Ipsum</span><span>has been the industry's standard dummy text ever since the 1500s, when an unknown</span><span>printer took a galley of type and scrambled it to make a type specimen book. It has</span><span>survived not only five centuries, but also the leap into electronic typesetting, remaining</span><span>essentially unchanged.</span></p>
    </article>
    <article class="post" style="top:347px">
      <div class="post-media" role="img" aria-label="Photo of a phone on a stand beside an open laptop on a desk"></div>
      <h2 class="post-title">Lorem ipsum Lorem ipsum Lorem.</h2>
      <p class="post-meta">by <a href="#">John</a> | Jan 27, 2017 <a href="#">California</a></p>
      <p class="post-excerpt"><span>Lorem Ipsum is simply dummy text of the printing and typesetting industry. Lorem Ipsum</span><span>has been the industry's standard dummy text ever since the 1500s, when an unknown</span><span>printer took a galley of type and scrambled it to make a type specimen book. It has</span><span>survived not only five centuries, but also the leap into electronic typesetting, remaining</span><span>essentially unchanged.</span></p>
    </article>
    <article class="post" style="top:689px">
      <div class="post-media" role="img" aria-label="Photo of a phone on a stand beside an open laptop on a desk"></div>
      <h2 class="post-title">Lorem ipsum Lorem ipsum Lorem.</h2>
      <p class="post-meta">by <a href="#">John</a> | Jan 27, 2017 <a href="#">California</a></p>
      <p class="post-excerpt"><span>Lorem Ipsum is simply dummy text of the printing and typesetting industry. Lorem Ipsum</span><span>has been the industry's standard dummy text ever since the 1500s, when an unknown</span><span>printer took a galley of type and scrambled it to make a type specimen book. It has</span><span>survived not only five centuries, but also the leap into electronic typesetting, remaining</span><span>essentially unchanged.</span></p>
    </article>
  </main>

  <aside class="sidebar">This SideBar</aside>

  <footer class="site-footer">
    <p class="copyright">@ Copyright www.example.com All Right Reserved</p>
    <div class="social-links" aria-label="Social links">
      <span></span><span></span><span></span><span></span>
    </div>
  </footer>
</body>
</html>
```